Drag Show Flyer

We are holding a Drag Show, we are looking for something fun and exciting, over the top is a must.

Show Date: Saturday September 2nd 2017
Venue: Pelican Row Cafe Bunbury
Doors open 7pm
Tickets: $50 per person, includes glass of sparkling on arrival and canapes
Tickets available at the Venue or from ticketloom.com.au

Target Market(s)

Female, Hens Party, LBGT

Industry/Entity Type

Entertainment

Colors

Designer to choose colors to be used in the design.

Requirements
Must have
• Show Date: Saturday September 2nd 2017
• Venue: Pelican Row Cafe Bunbury
• Doors open 7pm
• Tickets: $50 per person, includes glass of sparkling on arrival and canapes
• Tickets available at the Venue or from ticketloom.com.au

```html
<!DOCTYPE html>
<html lang="en">
<head>
<meta charset="utf-8">
<title>Drag Show Flyer</title>
<link href="https://fonts.googleapis.com/css2?family=Russo+One&family=Oswald:wght@500;700&family=Roboto:ital,wght@0,400;0,700;1,400&display=swap" rel="stylesheet">
<style>
  :root {
    --backdrop: #a3a4a8;
    --ink: #0a0612;
    --white: #ffffff;
    --pink: #e5177e;
    --yellow: #fff200;
    --purple: #7a2bd8;
    --blue: #2a7de1;
    --cyan: #31d2e0;
  }
  * { margin: 0; padding: 0; box-sizing: border-box; }
  html, body { width: 1200px; height: 1182px; overflow: hidden; }
  body { background: var(--backdrop); position: relative; font-family: "Roboto", Arial, sans-serif; }

  .flyer {
    position: absolute; left: 270px; top: 106px;
    width: 660px; height: 934px; overflow: hidden;
    background: var(--ink);
  }
  .stage-lights {
    position: absolute; left: 0; top: 420px; width: 660px; height: 514px;
    background:
      radial-gradient(ellipse at 90% 35%, rgba(49,210,224,.75), transparent 45%),
      radial-gradient(ellipse at 15% 70%, rgba(165,70,240,.85), transparent 55%),
      linear-gradient(160deg, #12081e 0%, #3a1580 45%, #2a4fc8 75%, #5a2bd0 100%);
  }
  .photo {
    position: absolute; left: 0; top: 0; width: 660px; height: 500px;
    background:
      radial-gradient(ellipse at 52% 30%, rgba(245,200,60,.55), transparent 28%),
      radial-gradient(ellipse at 85% 40%, rgba(230,40,150,.8), transparent 40%),
      linear-gradient(90deg, #7a1414 0%, #b3262a 25%, #5b2340 55%, #a2287e 80%, #7c1d64 100%);
    -webkit-mask-image: linear-gradient(180deg, #000 70%, transparent 100%);
            mask-image: linear-gradient(180deg, #000 70%, transparent 100%);
  }

  .title {
    position: absolute; left: 70px; width: 540px;
    font-family: "Russo One", Impact, sans-serif;
    color: var(--white); font-size: 128px; line-height: 1;
    letter-spacing: 14px; text-shadow: 0 0 18px rgba(229,23,126,.8);
    transform: rotate(-3deg); transform-origin: left bottom;
  }
  .title--drag { top: 350px; }
  .title--show { top: 460px; left: 78px; }

  .date-band {
    position: absolute; left: 82px; top: 580px; width: 512px; height: 50px;
    background: var(--pink);
    transform: rotate(-4deg); transform-origin: left top;
    font-family: "Oswald", "Arial Narrow", sans-serif; font-style: italic;
    display: flex; align-items: flex-end; padding: 0 0 0 14px; white-space: nowrap;
  }
  .date-band__day { color: var(--yellow); font-size: 58px; font-weight: 700; line-height: 1; margin-bottom: -12px; }
  .date-band__date { color: var(--ink); font-size: 30px; font-weight: 500; line-height: 1; margin: 0 0 6px 14px; }

  .venue {
    position: absolute; left: 143px; top: 628px; width: 390px; height: 180px;
    background: var(--ink);
    clip-path: polygon(2% 8%, 30% 2%, 60% 6%, 96% 0, 100% 30%, 97% 60%, 100% 88%, 70% 94%, 40% 100%, 4% 95%, 0 60%, 3% 35%);
    color: var(--white); text-align: center; padding-top: 40px;
  }
  .venue__label, .venue__name { font-weight: 700; font-size: 21px; line-height: 1.1; }
  .venue__doors { color: var(--pink); font-weight: 700; font-size: 16px; margin-top: 12px; }

  .tickets {
    position: absolute; left: -10px; top: 838px; width: 330px; height: 82px;
    background: var(--yellow);
    transform: rotate(-6deg); transform-origin: left top;
    padding: 8px 0 0 30px; color: var(--ink);
  }
  .tickets__line { font-family: "Oswald", "Arial Narrow", sans-serif; font-weight: 500; font-size: 24px; line-height: 1; white-space: nowrap; }
  .tickets__price { color: var(--pink); font-size: 40px; font-weight: 700; }
  .tickets__note { font-size: 11px; margin-top: 2px; }

  .footer {
    position: absolute; left: 0; top: 0; width: 660px; height: 934px; pointer-events: none;
  }
  .footer__info {
    position: absolute; left: 96px; top: 908px;
    font-size: 10.5px; font-style: italic; color: var(--ink); white-space: nowrap;
  }
  .footer__info a { color: var(--pink); text-decoration: none; }

  .sponsor { position: absolute; top: 881px; font-size: 11px; font-weight: 700; color: var(--ink); display: flex; align-items: center; gap: 5px; }
  .sponsor--venue { left: 391px; width: 83px; height: 35px; background: var(--ink); color: var(--white); justify-content: center; font-size: 10px; }
  .sponsor--group { left: 490px; }
  .sponsor__dot { width: 36px; height: 36px; border-radius: 50%; background: var(--ink); }
  .sponsor--group span { width: 50px; line-height: 1.05; }
  .sponsor--rouge { left: 585px; width: 50px; height: 44px; top: 878px; background: #e8e8ea; justify-content: center; text-align: center; font-size: 9px; }
</style>
</head>
<body>
  <main class="flyer">
    <div class="stage-lights" role="img" aria-label="Glowing purple and blue disco dot light backdrop"></div>
    <div class="photo" role="img" aria-label="Photo of drag performers in colourful wigs lounging on red booths in a nightclub"></div>

    <h1>
      <span class="title title--drag">DRAG</span>
      <span class="title title--show">SHOW</span>
    </h1>

    <div class="date-band">
      <span class="date-band__day">SATURDAY</span>
      <span class="date-band__date">SEPTEMBER.2ND.2017</span>
    </div>

    <section class="venue">
      <p class="venue__label">Venue:</p>
      <p class="venue__name">Pelican Row Cafe Bunbury</p>
      <p class="venue__doors">DOORS OPEN 7PM</p>
    </section>

    <section class="tickets">
      <p class="tickets__line">TICKETS: <span class="tickets__price">$50</span> PER PERSON</p>
      <p class="tickets__note">includes glass of sparkling on arrival and canapes</p>
    </section>

    <svg class="footer" viewBox="0 0 660 934" aria-hidden="true">
      <polygon points="0,914 660,842 660,934 0,934" fill="#ffffff"/>
    </svg>
    <p class="footer__info">Tickets available at the Venue or from <a href="#">ticketloom.com.au</a></p>

    <div class="sponsor sponsor--venue">Pelican Row Cafe</div>
    <div class="sponsor sponsor--group"><div class="sponsor__dot"></div><span>Gilded Circle Group</span></div>
    <div class="sponsor sponsor--rouge">Rouge Hour</div>
  </main>
</body>
</html>
```